Word Page Templates x 5

1 x Letterhead Template with Header and Footer able to be printed to paper and pdf with non blurry resolution
- File attached looks ok on computer screen but does not print the same
- We are wanting it to print like it looks on the screen
- We are wanting it to print not fuzzy in resolution
- We are wanting the banner to be on the absolute edge of the page like it is on the computer screen
- We are needing to print this to paper and pdf with perfect resolution and colour

Please can someone help us!!

I have provided the logo files in our posession. If better resolutions are required please let us know.

We are also wanting 4 simple page templates to be setup in Landscape and Portrait orientation as well once we are happy with the letterhead that is provided samples have been provided
Updates

Hi all I have the vector files available now along with a Colour profile

Requirements
Must have
• Clear when printed on A4 Paper
Should not have
• Blurry images, Colour must be correct (same as Logo) - Please reference our website if need be ..... vornal.com.au

```html
<!DOCTYPE html>
<html lang="en">
<head>
<meta charset="utf-8">
<title>Lanemark Clear – Letterhead</title>
<link href="https://fonts.googleapis.com/css2?family=Mulish:wght@400;600;700&display=swap" rel="stylesheet">
<style>
  :root {
    --backdrop: #d2d3d5;
    --paper: #ffffff;
    --brand-blue: #1f4e8c;
    --band-green: #c4dccb;
    --band-blue: #bac9dc;
    --footer-blue: #235a8c;
    --footer-green: #2f8045;
  }
  * { margin: 0; padding: 0; box-sizing: border-box; }
  html, body {
    width: 1200px; height: 793px; overflow: hidden;
    background: var(--backdrop);
    font-family: "Mulish", sans-serif;
  }
  .letterhead {
    position: absolute;
    background: var(--paper);
    overflow: hidden;
  }
  .letterhead--portrait { left: 152px; top: 146px; width: 355px; height: 501px; }
  .letterhead--landscape { left: 547px; top: 219px; width: 501px; height: 354px; }

  .header-band { position: absolute; left: 0; top: 0; width: 100%; height: 90px; }

  .brand-name {
    position: absolute;
    color: var(--brand-blue);
    font-weight: 700;
    font-size: 12px;
    letter-spacing: 0.1px;
    white-space: nowrap;
  }
  .letterhead--portrait .brand-name { left: 18px; top: 28px; }
  .letterhead--landscape .brand-name { left: 24px; top: 34px; }

  .contact-list {
    position: absolute;
    list-style: none;
    color: var(--brand-blue);
    font-size: 4.8px;
    line-height: 9px;
  }
  .letterhead--portrait .contact-list { left: 212px; top: 13px; }
  .letterhead--landscape .contact-list { left: 348px; top: 21px; }
  .contact-list .label { display: inline-block; width: 10.5px; font-weight: 700; }

  .footer-bar {
    position: absolute; left: 0; bottom: 0; width: 100%; height: 9px;
    background: linear-gradient(90deg, var(--footer-blue), var(--footer-green));
  }
</style>
</head>
<body>
  <svg width="0" height="0" style="position:absolute">
    <defs>
      <linearGradient id="band-fade" x1="0" x2="1" y1="0" y2="0">
        <stop offset="0" stop-color="var(--band-green)"/>
        <stop offset="0.55" stop-color="var(--band-green)"/>
        <stop offset="1" stop-color="var(--band-blue)"/>
      </linearGradient>
    </defs>
  </svg>

  <section class="letterhead letterhead--portrait">
    <svg class="header-band" viewBox="0 0 355 90" aria-hidden="true">
      <path fill="url(#band-fade)" d="M0,62 H323 C330,60 331,50 328,45 C325,38 320,31 315,26 C320,21 323,19 326,20 C334,23 339,33 337,44 C335,60 320,73 305,73 H0 Z"/>
    </svg>
    <div class="brand-name">Lanemark Clear</div>
    <ul class="contact-list">
      <li><span class="label">A.</span>PO Box 2380, Tallowood 4228 QLD</li>
      <li><span class="label">P.</span>0412 555 318</li>
      <li><span class="label">E.</span>info@lanemarkclear.com.au</li>
      <li><span class="label">W.</span>www.lanemarkclear.com.au</li>
    </ul>
    <div class="footer-bar"></div>
  </section>

  <section class="letterhead letterhead--landscape">
    <svg class="header-band" viewBox="0 0 501 90" aria-hidden="true">
      <path fill="url(#band-fade)" d="M0,68 H459 C466,66 467,56 464,51 C461,44 456,37 451,32 C456,27 459,25 462,26 C470,29 475,39 473,50 C471,66 456,79 441,79 H0 Z"/>
    </svg>
    <div class="brand-name">Lanemark Clear</div>
    <ul class="contact-list">
      <li><span class="label">A.</span>PO Box 2380, Tallowood 4228 QLD</li>
      <li><span class="label">P.</span>0412 555 318</li>
      <li><span class="label">E.</span>info@lanemarkclear.com.au</li>
      <li><span class="label">W.</span>www.lanemarkclear.com.au</li>
    </ul>
    <div class="footer-bar"></div>
  </section>
</body>
</html>
```